Construction company focused on concrete and shed construction.

We need to update our current business card for ridgeforgebuilds.com.au we would like an eye catching design with blue, grey and white incorporating our current logo.
Our company started off in concreting and due to varying factors we have expanded to include shed construction as well.
This has led to our current Logo looking a little out of place and somehow need to use the card to bring in the shed construction side of the business while not having to change current concrete look "KESTRO" logo as we already have this incorporated into our company clothing and are not willing to change this yet.
Photo image attached for inspiration/ visual reference of type of work, not to be used on final design.
Please no cheesy designs of men in hard hats and tools
Final design should demonstrate a modern and service focused company.

Target Market(s)

Farmers, Business owners, Developers, Architects, Commercial project delivery

Industry/Entity Type

Construction Company

Contact Information for Business Card

Kestro Constructions.
7b Harlow st
South Launceston Tas
03 62918873

Font styles to use
Other font styles liked:
• see font in logo

Colors
3176b5
b2b2b2

Requirements
Must have
• Easy to read font,
• good contrast between back ground and writing
Nice to have
• Modern and corporate look with a fun but professional image.
Should not have
• Comic images or shadow images of tools/ people.

```html
<!DOCTYPE html>
<html lang="en">
<head>
<meta charset="utf-8">
<title>Kestro Group Constructions – Business Card</title>
<link rel="stylesheet" href="https://fonts.googleapis.com/css2?family=Montserrat:wght@400;500;700&family=Questrial&display=swap">
<style>
  :root {
    --brand-blue: #145a97;
    --brand-blue-light: #8fc1ea;
    --charcoal: #22292f;
    --grey: #b2b2b2;
    --grey-dark: #4a4f55;
    --white: #ffffff;
    --backdrop: #f4f4f4;
  }
  * { box-sizing: border-box; margin: 0; padding: 0; }
  html, body {
    width: 1200px;
    height: 800px;
    overflow: hidden;
    background: var(--backdrop);
  }
  .card {
    position: absolute;
    width: 560px;
    height: 320px;
    overflow: hidden;
    box-shadow: 0 6px 18px rgba(0, 0, 0, 0.12);
  }

  /* Back of card */
  .card-back {
    left: 60px;
    top: 60px;
    background: var(--brand-blue);
  }
  .card-back .brand-mark {
    position: absolute;
    left: 0;
    right: 0;
    top: 105px;
    display: flex;
    justify-content: center;
    align-items: center;
    gap: 14px;
  }
  .card-back .brand-dot {
    width: 46px;
    height: 46px;
    border-radius: 50%;
    background: var(--brand-blue-light);
  }
  .card-back .brand-name {
    font-family: "Montserrat", sans-serif;
    font-weight: 700;
    font-size: 40px;
    letter-spacing: 2px;
    color: var(--white);
  }
  .card-back .website {
    position: absolute;
    left: 0;
    right: 0;
    bottom: 62px;
    text-align: center;
    font-family: "Questrial", sans-serif;
    font-size: 19px;
    letter-spacing: 2px;
    color: var(--white);
  }

  /* Front of card */
  .card-front {
    left: 580px;
    top: 420px;
    background: var(--white);
  }
  .card-front .corner-art {
    position: absolute;
    inset: 0;
  }
  .card-front .brand-mark {
    position: absolute;
    left: 34px;
    top: 140px;
    display: flex;
    align-items: center;
    gap: 10px;
  }
  .card-front .brand-dot {
    width: 34px;
    height: 34px;
    border-radius: 50%;
    background: var(--brand-blue);
  }
  .card-front .brand-name {
    font-family: "Montserrat", sans-serif;
    font-weight: 700;
    font-size: 28px;
    letter-spacing: 1px;
    color: var(--grey-dark);
  }
  .company {
    position: absolute;
    left: 240px;
    top: 88px;
  }
  .company-name {
    font-family: "Montserrat", sans-serif;
    font-weight: 700;
    font-size: 36px;
    line-height: 1;
    color: var(--brand-blue);
  }
  .company-tagline {
    margin-top: 8px;
    font-family: "Montserrat", sans-serif;
    font-weight: 500;
    font-size: 12px;
    letter-spacing: 6.5px;
    color: var(--charcoal);
  }
  .contact-list {
    position: absolute;
    left: 252px;
    top: 178px;
    list-style: none;
    font-family: "Questrial", sans-serif;
    font-size: 14px;
    color: var(--charcoal);
  }
  .contact-item {
    display: flex;
    align-items: center;
    gap: 10px;
    margin-bottom: 8px;
  }
  .contact-icon {
    width: 20px;
    height: 20px;
    flex: none;
  }
</style>
</head>
<body>

  <section class="card card-back" aria-label="Business card back">
    <div class="brand-mark">
      <span class="brand-dot"></span>
      <span class="brand-name">KESTRO</span>
    </div>
    <p class="website">www.ridgeforgebuilds.com.au</p>
  </section>

  <section class="card card-front" aria-label="Business card front">
    <svg class="corner-art" viewBox="0 0 560 320" aria-hidden="true">
      <polygon points="430,0 560,0 560,96" fill="var(--brand-blue)"/>
      <polygon points="372,0 416,0 548,100 536,104" fill="var(--charcoal)"/>
      <polygon points="560,218 560,272 502,272" fill="var(--brand-blue)"/>
      <polygon points="0,214 0,320 140,320" fill="var(--brand-blue)"/>
      <polygon points="40,228 196,320 150,320 28,240" fill="var(--charcoal)"/>
    </svg>

    <div class="brand-mark">
      <span class="brand-dot"></span>
      <span class="brand-name">KESTRO</span>
    </div>

    <div class="company">
      <h1 class="company-name">Kestro Group</h1>
      <p class="company-tagline">CONSTRUCTIONS</p>
    </div>

    <ul class="contact-list">
      <li class="contact-item">
        <svg class="contact-icon" viewBox="0 0 20 20" aria-label="Phone">
          <circle cx="10" cy="10" r="10" fill="var(--brand-blue)"/>
          <path d="M7 5.2c.4-.3.9-.2 1.1.2l.9 1.6c.2.4.1.8-.2 1.1l-.6.5c.5 1.2 1.4 2.1 2.6 2.6l.5-.6c.3-.3.7-.4 1.1-.2l1.6.9c.4.2.5.7.2 1.1l-.8 1c-.4.5-1.1.7-1.7.4C9.3 12.8 7.2 10.7 6.2 8.3c-.3-.6-.1-1.300.4-1.7z" fill="var(--white)"/>
        </svg>
        <span>03 62918873</span>
      </li>
      <li class="contact-item">
        <svg class="contact-icon" viewBox="0 0 20 20" aria-label="Address">
          <circle cx="10" cy="10" r="10" fill="var(--brand-blue)"/>
          <path d="M10 4.5a3.6 3.6 0 0 0-3.6 3.6c0 2.7 3.6 6.9 3.6 6.9s3.6-4.2 3.6-6.9A3.6 3.6 0 0 0 10 4.5zm0 5a1.4 1.4 0 1 1 0-2.8 1.4 1.4 0 0 1 0 2.8z" fill="var(--white)"/>
        </svg>
        <span>7b Harlow st South Launceston Tas</span>
      </li>
    </ul>
  </section>

</body>
</html>
```